A card that says it all!

Hey there!
We are in need of a business card design for a facility service provider company named Kelbrook Works.
I would like a business card design that is not focus on a person but more on the company. A place for a QR code would be nice, and i will have that code direct to our request form online. "Scanner to schedule service" or "Scan to schedule a estimate". Something like that. Kelbrook Works is the Industry Leader in Facility Remodeling, Rollouts, and Capital Repairs

Target Market(s)

large facilities needing services such as remodels. HVAC, plumbing, electrical

Industry/Entity Type

Industry Leader in Facility Remodeling, Rollouts, and Capital Repairs

Contact Information for Business Card

phone number: 418.527.3096; email: info@kelbrookworks.us; Website: www.KelbrookWorks.us

Requirements
Must have
• sleak; classic
Should not have
• No houses or tools art

```html
<!DOCTYPE html>
<html lang="en">
<head>
<meta charset="utf-8">
<title>Kelbrook Works Business Card</title>
<link href="https://fonts.googleapis.com/css2?family=EB+Garamond:ital,wght@0,400;0,500;1,400&display=swap" rel="stylesheet">
<style>
  :root {
    --brand-blue: #17459c;
    --card-white: #f7f7f7;
    --ink: #3a3a3a;
    --divider: #8a8a8a;
    --page: #e9e7e3;
  }
  html, body {
    margin: 0;
    padding: 0;
    width: 1200px;
    height: 900px;
    overflow: hidden;
    background: var(--page);
    font-family: "EB Garamond", Georgia, serif;
  }
  .canvas {
    position: relative;
    width: 1200px;
    height: 900px;
  }
  .card {
    position: absolute;
    left: 285px;
    width: 630px;
    height: 360px;
    border-radius: 30px;
    box-shadow: 0 10px 24px rgba(0,0,0,0.18);
    overflow: hidden;
  }
  .card-front {
    top: 60px;
    background: var(--brand-blue);
    display: flex;
    align-items: center;
    justify-content: center;
  }
  .card-back {
    top: 480px;
    background: var(--card-white);
  }
  .wordmark {
    font-weight: 500;
    letter-spacing: 0.04em;
    line-height: 1;
    white-space: nowrap;
  }
  .card-front .wordmark {
    color: #ffffff;
    font-size: 54px;
  }
  .back-brand {
    position: absolute;
    left: 40px;
    top: 108px;
    width: 250px;
    text-align: center;
  }
  .card-back .wordmark {
    color: var(--brand-blue);
    font-size: 36px;
  }
  .divider {
    position: absolute;
    left: 312px;
    top: 46px;
    width: 1px;
    height: 180px;
    background: linear-gradient(to bottom, transparent, var(--divider) 20%, var(--divider) 80%, transparent);
  }
  .contact-list {
    position: absolute;
    left: 340px;
    top: 62px;
    margin: 0;
    padding: 0;
    list-style: none;
  }
  .contact-item {
    display: flex;
    align-items: center;
    gap: 12px;
    font-size: 21px;
    color: var(--ink);
    margin-bottom: 12px;
  }
  .contact-icon {
    width: 18px;
    height: 18px;
    flex: none;
    color: var(--brand-blue);
  }
  .tagline {
    position: absolute;
    left: 0;
    right: 0;
    bottom: 56px;
    margin: 0;
    text-align: center;
    font-style: italic;
    font-size: 21px;
    line-height: 1.3;
    color: var(--brand-blue);
  }
</style>
</head>
<body>
<main class="canvas">
  <section class="card card-front">
    <span class="wordmark">Kelbrook Works</span>
  </section>

  <section class="card card-back">
    <div class="back-brand">
      <span class="wordmark">Kelbrook Works</span>
    </div>
    <div class="divider"></div>
    <ul class="contact-list">
      <li class="contact-item">
        <svg class="contact-icon" viewBox="0 0 24 24" aria-hidden="true"><path fill="currentColor" d="M6.6 10.8a15 15 0 0 0 6.6 6.6l2.2-2.2a1 1 0 0 1 1-.25 11.4 11.4 0 0 0 3.6.57 1 1 0 0 1 1 1V20a1 1 0 0 1-1 1A17 17 0 0 1 3 4a1 1 0 0 1 1-1h3.5a1 1 0 0 1 1 1c0 1.25.2 2.45.57 3.57a1 1 0 0 1-.25 1z"/></svg>
        <span>418.527.3096</span>
      </li>
      <li class="contact-item">
        <svg class="contact-icon" viewBox="0 0 24 24" aria-hidden="true"><path fill="currentColor" d="M2 5h20v14H2z"/><path fill="none" stroke="#fff" stroke-width="1.6" d="M2.5 5.5 12 13l9.5-7.5M2.5 18.5l7-6.5M21.5 18.5l-7-6.5"/></svg>
        <span>info@kelbrookworks.us</span>
      </li>
      <li class="contact-item">
        <svg class="contact-icon" viewBox="0 0 24 24" aria-hidden="true"><g fill="none" stroke="currentColor" stroke-width="1.6"><circle cx="12" cy="12" r="9.5"/><ellipse cx="12" cy="12" rx="4.2" ry="9.5"/><path d="M2.5 12h19M4 7h16M4 17h16"/></g></svg>
        <span>www.KelbrookWorks.us</span>
      </li>
    </ul>
    <p class="tagline">Kelbrook Works is the Industry Leader in<br>Facility Remodeling, Rollouts, and Capital Repairs</p>
  </section>
</main>
</body>
</html>
```